Re-Design Website

Task Outline:
Re- Web design with call-to-action orientated .
Task Description:
■Our Service
Our service is call Zelvoria.
We are a mobile games only cross promotion and advertising platform.
■Reference WebSites
This will be few sites that is doing almost similar service
1.www.plumvexa.com
2.www.norquibe.com
3.www.duskorelo.net/ (japanese site, but don’t worry about the wordings.)
4.http://vintrosk.com/
■ Little Details
In a nutshell, we are advertising company for mobile games, which offer to show fullscreen ads(interstitial ads), standard banner ads, larger banner ads, icon ads and recommendation ads.
Our current site is at www.zelvoria.net. (No copy write job has been done for contents yet, don’t worry about that)
Requirements:
● flat design, play well with white space ( we love the halbrimo.com design )
● A straight to the point landing image
● All contents are fit in a 1 long page -Once scrolled down to contents. It needs to be very neat and clear on how it deliver the message through images and contents.
● Clean, simple. Reduce wordings; focus on graphic-information to intrigue response.
● We would like to reduce navigation activities and to have an outstanding Call To Action (CTA) button, which to convert user into conversion funnel (example, Learn More, to download our eBooks, Sign Up Now, Join)
● Interesting Facebook/Twitter button to build variability.
● Desired user experience, that able to convert information to graphical content. (Like above the fold like Vintrosk.com)
Please refer to a few reference images:
1. *upload a few sushi/ice cream/reon/images for them to use”
Pages to design
1. Landing page
2. About Us
3. Sign in & Sign Up (Must be simple and friendly)
Logo:
We are open to suggestions.
Color preference: (We open for suggestions) ---> WE ARE NOT GOING TO USE ORANGE
● color – change corporate Identity color. The background color can be darker above to fold to make it more stylish.
● 3 tone colors on a web page (something like halbrimo.com) → For Example (Refering to Hal Brimo : Main Color : Blue, Base Color : Gray… White, Tone Color : Green) ---> Sure you can play around with it.
● fun and energetic color tone (since we are strongly related with mobile games)
Font:
● clear typography - similar to product identity
● helvetica neue light (currently are using but we are open to suggestion)
Target Market:
● Game publisher
● Game Developer
● Partners: Advertising Agencies, (Business 2 Business)
● ASEAN Countries. ie Taiwan, Japan, China, HK...etc
Deadline:
● 31st December 2013

```html
<!DOCTYPE html>
<html lang="en">
<head>
<meta charset="utf-8">
<title>Zelvoria – in-app monetization</title>
<link rel="stylesheet" href="https://fonts.googleapis.com/css2?family=Arimo:wght@400;700&family=Inter:wght@300;400;600;700&display=swap">
<style>
  :root {
    --backdrop: #666666;
    --navy: #2f3e52;
    --navy-text: #253447;
    --blue: #3a96dc;
    --white: #ffffff;
    --body-text: #1f2b3a;
    --muted: #7d8792;
    --nav-text: #aab4c0;
    --pager-bg: #dcdfe3;
    --pager-dot: #ffffff;
    --card-border: #2a3747;
  }
  * { box-sizing: border-box; margin: 0; padding: 0; }
  html, body { width: 1200px; height: 1000px; overflow: hidden; }
  body { background: var(--backdrop); font-family: "Arimo", Arial, sans-serif; color: var(--body-text); }
  .page { position: absolute; left: 284px; top: 0; width: 632px; height: 1000px; background: var(--white); }
  .abs { position: absolute; }

  /* header */
  .site-header { position: absolute; left: 0; top: 0; width: 632px; height: 54px; background: var(--navy); }
  .brand { position: absolute; left: 68px; top: 24px; font-family: "Inter", sans-serif; font-weight: 300; font-size: 21px; color: var(--white); letter-spacing: -0.5px; }
  .main-nav { position: absolute; top: 33px; left: 289px; display: flex; gap: 0; font-family: "Inter", sans-serif; font-weight: 300; font-size: 11px; color: var(--nav-text); }
  .main-nav span { position: absolute; white-space: nowrap; }
  .btn { position: absolute; display: flex; align-items: center; justify-content: center; font-family: "Arimo", sans-serif; font-weight: 700; border-radius: 2px; }
  .btn-primary { background: var(--blue); color: var(--white); }
  .header-cta { left: 513px; top: 31px; width: 50px; height: 18px; font-size: 7px; }

  /* features */
  .feature-title { position: absolute; left: 68px; font-family: "Arimo", sans-serif; font-weight: 700; font-size: 16.5px; line-height: 19px; color: var(--navy-text); }
  .feature-text { position: absolute; left: 68px; width: 118px; font-size: 7.6px; line-height: 12.8px; color: var(--body-text); }

  .hero-title { position: absolute; left: 195px; top: 98px; font-family: "Inter", sans-serif; font-weight: 300; font-size: 21.5px; line-height: 27px; color: var(--navy-text); letter-spacing: -0.3px; }
  .copy { position: absolute; left: 195px; width: 370px; font-size: 7.9px; line-height: 12.3px; color: var(--body-text); text-align: justify; }

  .slide-text { position: absolute; left: 195px; top: 332px; width: 145px; font-family: "Inter", sans-serif; font-weight: 300; font-size: 15.5px; line-height: 19.2px; color: var(--muted); }
  .slide-visual { position: absolute; left: 352px; top: 298px; width: 211px; height: 139px; background: linear-gradient(135deg, #1b1d22 0%, #3c5a3e 45%, #c9a27f 80%, #f1e6dd 100%); border-radius: 6px 0 0 0; }

  .pager { position: absolute; left: 230px; top: 453px; width: 300px; height: 20px; background: var(--pager-bg); border-radius: 2px; }
  .pager svg { display: block; }

  /* cards */
  .ad-band { position: absolute; left: 0; top: 690px; width: 632px; height: 252px; background: var(--blue); }
  .ad-card { position: absolute; top: 681px; width: 114px; height: 202px; background: var(--white); border: 1.5px solid var(--card-border); border-radius: 4px; }
  .ad-card .thumb { position: absolute; left: 4px; top: 4px; width: 103px; height: 92px; border-radius: 2px; }
  .ad-card h3 { position: absolute; left: 0; width: 100%; text-align: center; font-size: 10.5px; line-height: 13px; font-weight: 700; color: var(--navy-text); }
  .ad-card p { position: absolute; left: 6px; width: 99px; top: 127px; text-align: center; font-size: 6.6px; line-height: 9.2px; color: var(--muted); }
  .card-btn { left: 26px; top: 172px; width: 60px; height: 18px; font-size: 6.5px; background: var(--navy); color: var(--white); }

  /* footer */
  .site-footer { position: absolute; left: 0; top: 942px; width: 632px; height: 58px; background: var(--navy); }
  .copyright { position: absolute; left: 74px; top: 27px; font-size: 6.5px; color: var(--nav-text); }
  .social-badge { position: absolute; top: 16px; width: 32px; height: 26px; }
  .btn-outline { left: 449px; top: 20px; width: 51px; height: 18px; font-size: 7px; border: 1.2px solid var(--white); color: var(--white); }
  .footer-cta { left: 513px; top: 20px; width: 50px; height: 18px; font-size: 7px; }
</style>
</head>
<body>
<div class="page">
  <header class="site-header">
    <div class="brand">Zelvoria</div>
    <nav class="main-nav">
      <span style="left:0">about</span>
      <span style="left:53px">how it works</span>
      <span style="left:137px">applications</span>
    </nav>
    <div class="btn btn-primary header-cta">Sign up</div>
  </header>

  <!-- feature: first day -->
  <svg class="abs" style="left:68px;top:108px" width="40" height="40" viewBox="0 0 40 40" aria-hidden="true">
    <rect x="0" y="0" width="40" height="40" rx="3" fill="#2f6fb8"/>
    <rect x="4" y="7" width="32" height="29" fill="#ffffff"/>
    <text x="20" y="30" text-anchor="middle" font-family="Arimo, sans-serif" font-weight="700" font-size="19" fill="#d83a2e">1</text>
  </svg>
  <h2 class="feature-title" style="top:161px">First day<br>monetization</h2>
  <p class="feature-text" style="top:204px">Lorem ipsum dolor sit amet, consectetur adipiscing elit. Cras imperdiet pharetra erat, sed vulputate mauris mattis sed.</p>

  <h1 class="hero-title">Welcome to your favourite<br>in-app monetization service</h1>
  <p class="copy" style="top:162px">Lorem ipsum dolor sit amet, consectetur adipiscing elit. Cras imperdiet pharetra erat, sed vulputate mauris mattis sed. Fusce sit amet ultrices nunc. Praesent erat tellus, tincidunt in diam quis, tempus viverra dui. Vestibulum cursus mi sem, sit amet consectetur felis gravida non. Etiam dignissim ultrices turpis, sit amet tempor lorem commodo ut. Cras varius sem sit amet magna semper, et varius lorem dignissim. Mauris euismod malesuada metus, eu mattis est. Donec posuere, nulla facilisis tincidunt lobortis, orci tellus sollicitudin tellus, nec mattis mi urna eu tortor. Proin ut porta mauris, id porttitor dolor. Cum sociis natoque penatibus et magnis dis parturient montes, nascetur ridiculus mus. Donec at quam non est vestibulum sagittis ac ut elit. Donec sit amet massa a erat pharetra dignissim quis vel augue. Ut tristique sapien non iaculis lobortis.</p>

  <!-- feature: recurring -->
  <svg class="abs" style="left:68px;top:284px" width="53" height="53" viewBox="0 0 53 53" aria-hidden="true">
    <circle cx="26.5" cy="26.5" r="26.5" fill="#2f73c0"/>
    <path d="M26.5 26.5 C21 19 12 19 12 26.5 C12 34 21 34 26.5 26.5 C32 19 41 19 41 26.5 C41 34 32 34 26.5 26.5 Z" fill="none" stroke="#f2c21b" stroke-width="4.5"/>
  </svg>
  <h2 class="feature-title" style="top:345px">Recurring<br>items</h2>
  <p class="feature-text" style="top:388px">Lorem ipsum dolor sit amet, consectetur adipiscing elit. Cras imperdiet pharetra erat, sed vulputate mauris mattis sed.</p>

  <p class="slide-text">Lorem ipsum dolor sit amet, consectetur adipiscing elit. Ut tristique sapien</p>
  <div class="slide-visual" role="img" aria-label="Hand holding a smartphone showing a game promotion"></div>

  <div class="pager">
    <svg width="300" height="20" viewBox="0 0 300 20" aria-hidden="true">
      <rect x="0" y="0" width="24" height="20" fill="#cfd3d8"/>
      <rect x="276" y="0" width="24" height="20" fill="#cfd3d8"/>
      <path d="M15 6 L9 10 L15 14 Z" fill="#ffffff"/>
      <path d="M285 6 L291 10 L285 14 Z" fill="#ffffff"/>
      <g fill="#ffffff">
        <circle cx="38" cy="10" r="5"/>
        <circle cx="52" cy="10" r="3.5"/><circle cx="66" cy="10" r="3.5"/><circle cx="80" cy="10" r="3.5"/>
        <circle cx="94" cy="10" r="3.5"/><circle cx="108" cy="10" r="3.5"/><circle cx="122" cy="10" r="3.5"/>
        <circle cx="136" cy="10" r="3.5"/><circle cx="150" cy="10" r="3.5"/><circle cx="164" cy="10" r="3.5"/>
        <circle cx="178" cy="10" r="3.5"/><circle cx="192" cy="10" r="3.5"/>
        <circle cx="220" cy="10" r="3.5"/><circle cx="234" cy="10" r="3.5"/><circle cx="248" cy="10" r="3.5"/><circle cx="262" cy="10" r="3.5"/>
      </g>
      <text x="38" y="12.5" text-anchor="middle" font-family="Arimo, sans-serif" font-size="6.5" fill="#8a939c">1</text>
      <circle cx="206" cy="10" r="7" fill="#253447"/>
      <text x="206" y="12.5" text-anchor="middle" font-family="Arimo, sans-serif" font-weight="700" font-size="6.5" fill="#ffffff">14</text>
    </svg>
  </div>

  <!-- feature: customisation -->
  <div class="abs" style="left:68px;top:468px;width:53px;height:53px;border-radius:50%;background:conic-gradient(#d2452f,#f0a72a,#7b4aa3,#2f73c0,#3b9c5a,#d2452f)" role="img" aria-label="Colourful geometric customisation emblem"></div>
  <h2 class="feature-title" style="top:529px">Great<br>customisation</h2>
  <p class="feature-text" style="top:573px">Lorem ipsum dolor sit amet, consectetur adipiscing elit. Cras imperdiet pharetra erat, sed vulputate mauris mattis sed.</p>

  <p class="copy" style="top:497px">Lorem ipsum dolor sit amet, consectetur adipiscing elit. Cras imperdiet pharetra erat, sed vulputate mauris mattis sed. Fusce sit amet ultrices nunc. Praesent erat tellus, tincidunt in diam quis, tempus viverra dui. Vestibulum cursus mi sem, sit amet consectetur felis gravida non. Etiam dignissim ultrices turpis, sit amet tempor lorem commodo ut. Cras varius sem sit amet magna semper, et varius lorem dignissim. Mauris euismod malesuada metus, eu mattis est. Donec posuere, nulla facilisis tincidunt lobortis, orci tellus sollicitudin tellus, nec mattis mi urna eu tortor. Proin ut porta mauris, id porttitor dolor. Cum sociis natoque penatibus et magnis dis parturient montes, nascetur ridiculus mus. Donec at quam non est vestibulum sagittis ac ut elit. Donec sit amet massa a erat pharetra dignissim quis vel augue. Ut tristique sapien non iaculis lobortis.</p>

  <!-- ad formats -->
  <div class="ad-band"></div>

  <article class="ad-card" style="left:69px">
    <div class="thumb" role="img" aria-label="Ice cream shop game screenshot" style="background:linear-gradient(180deg,#f3c4c8,#c98a5e 60%,#f6e2d6)"></div>
    <h3 style="top:112px">Fullscreen ads</h3>
    <p>Lorem ipsum dolor sit amet, consectetur adipiscing elit. Cras imperdiet pharetra erat, sed vulputate mauris mattis sed.</p>
    <div class="btn card-btn">How it works</div>
  </article>

  <article class="ad-card" style="left:195px">
    <div class="thumb" role="img" aria-label="Sushi game promotional banner" style="background:linear-gradient(180deg,#ffffff 10%,#f2d8c8 50%,#9fb6c8)"></div>
    <h3 style="top:96px">Standard and<br>larger ads</h3>
    <p>Lorem ipsum dolor sit amet, consectetur adipiscing elit. Cras imperdiet pharetra erat, sed vulputate mauris mattis sed.</p>
    <div class="btn card-btn">How it works</div>
  </article>

  <article class="ad-card" style="left:322px">
    <div class="thumb" role="img" aria-label="Game app icon" style="left:10px;top:8px;width:92px;height:92px;border-radius:14px;background:linear-gradient(160deg,#7fd6b8,#3fae8f)"></div>
    <h3 style="top:112px">Icon ads</h3>
    <p>Lorem ipsum dolor sit amet, consectetur adipiscing elit. Cras imperdiet pharetra erat, sed vulputate mauris mattis sed.</p>
    <div class="btn card-btn">How it works</div>
  </article>

  <article class="ad-card" style="left:449px">
    <div class="thumb" role="img" aria-label="Ice cream game recommendation screenshot" style="background:linear-gradient(180deg,#f7dfe2,#e8a9a6 50%,#b86c52)"></div>
    <h3 style="top:112px">Recommandations</h3>
    <p>Lorem ipsum dolor sit amet, consectetur adipiscing elit. Cras imperdiet pharetra erat, sed vulputate mauris mattis sed.</p>
    <div class="btn card-btn">How it works</div>
  </article>

  <footer class="site-footer">
    <div class="copyright">Copyright 2014 (c) Zelvoria</div>
    <svg class="social-badge" style="left:271px" viewBox="0 0 32 26" aria-hidden="true">
      <circle cx="16" cy="12" r="11" fill="#3b6fb5" stroke="#dfe6ee" stroke-width="2"/>
      <rect x="2" y="18" width="28" height="6" rx="2" fill="#dfe6ee"/>
    </svg>
    <svg class="social-badge" style="left:332px" viewBox="0 0 32 26" aria-hidden="true">
      <circle cx="16" cy="12" r="11" fill="#3d9ee0" stroke="#dfe6ee" stroke-width="2"/>
      <rect x="2" y="18" width="28" height="6" rx="2" fill="#dfe6ee"/>
    </svg>
    <div class="btn btn-outline">About us</div>
    <div class="btn btn-primary footer-cta">Sign up</div>
  </footer>
</div>
</body>
</html>
```